Truck Wraps for Hearthwell Building Trucks

We need a design for our Construction truck wraps. It will need to incorporate the company logo and colors and well as some text which we will provide.
The wrap will be the same on two panels of the truck (the large panels) with a separate (but similar ) design for the back gate.

I have included pictures of the existing design and an example of the type of design we want for the new one.

I am including some branding guidelines. I am also including examples of our logo, which needs to be updated to the new color scheme.

The photo of the van (named truck) is a general idea of the feel we are looking for.
the design needs to have the words

DONATE* VOLUNTEER *ADVOCATE* APPLY

Please note...when using green and blue, the codes ar the blue has a Hex code of 00afd7

The green has a hex code c4d600

Industry/Entity Type

Non Profit construction

Font styles to use
Sans Serif
Other font styles liked:
• Neue Haas Gotesk or Arial . Minion Pro or Palatino

Colors
0054AA
0677BA
7BADD7
CADEEF
E8F1F8
00AB8E
00BBA5
67D7C9
C6EFE9
E9F9F6

Requirements
Must have
• Company Logo and Shelterbridge Alliance of Greater Miami Logo

```html
<!DOCTYPE html>
<html lang="en">
<head>
<meta charset="utf-8">
<title>Hearthwell Building – Truck Side Panel</title>
<link rel="stylesheet" href="https://fonts.googleapis.com/css2?family=Jost:wght@400;700&display=swap">
<style>
  :root {
    --panel-white: #ffffff;
    --panel-edge: #d9dcdf;
    --ink-black: #111111;
    --brand-blue: #1f64a8;
    --brand-green: #4bb848;
    --page-bg: #eef0f2;
  }
  * { box-sizing: border-box; margin: 0; padding: 0; }
  html, body {
    width: 1200px;
    height: 687px;
    overflow: hidden;
    background: var(--page-bg);
    font-family: "Jost", "Futura", sans-serif;
  }
  .side-panel {
    position: absolute;
    left: 30px;
    top: 60px;
    width: 1140px;
    height: 567px;
    background: var(--panel-white);
    border: 6px solid var(--panel-edge);
    border-radius: 4px;
  }
  .brand-mark {
    position: absolute;
    left: 90px;
    top: 150px;
    width: 520px;
    display: flex;
    align-items: center;
    gap: 28px;
  }
  .brand-mark__dot {
    flex: none;
    width: 90px;
    height: 90px;
    border-radius: 50%;
    background: var(--brand-green);
  }
  .brand-mark__name {
    color: var(--brand-blue);
    font-weight: 700;
    font-size: 52px;
    line-height: 1.05;
  }
  .call-to-action {
    position: absolute;
    right: 58px;
    top: 92px;
    text-align: right;
    color: var(--ink-black);
    font-size: 62px;
    line-height: 70px;
    letter-spacing: 1px;
    list-style: none;
  }
  .call-to-action__light { font-weight: 400; }
  .call-to-action__bold { font-weight: 700; }
  .web-address {
    position: absolute;
    right: 58px;
    top: 420px;
    color: var(--brand-blue);
    font-weight: 700;
    font-size: 34px;
  }
</style>
</head>
<body>
  <section class="side-panel" aria-label="Truck side panel wrap">
    <div class="brand-mark">
      <span class="brand-mark__dot"></span>
      <span class="brand-mark__name">Shelterbridge Alliance of Greater Miami</span>
    </div>
    <ul class="call-to-action">
      <li class="call-to-action__light">DONATE</li>
      <li class="call-to-action__bold">VOLUNTEER</li>
      <li class="call-to-action__light">ADVOCATE</li>
      <li class="call-to-action__bold">APPLY</li>
    </ul>
    <p class="web-address">shelterbridgemiami.org</p>
  </section>
</body>
</html>
```